Stock Broking Firm - Web Design Project

We are looking at doing a full re-design of our home page and content page and moving the majority of our content over to DNN.

Phase 1 : Website redesign www.kpwealthdesk.com.au

The current design is too washed out, boring and has no call to action buttons.

Solution:

KP Wealthdesk is looking for a brighter/ cleaner redesign with a few stand out call to action buttons.

• Banner with logo across the top horizontally - Bright blue logo on white background similar to www.dailyledgerpress.com.au - CALL 1300 482 917 - Follow on Twitter / Facebook
• Horizontal menu bar - professional looking. - Home - About Us- Our Services - Membership - Open an Account - Become a member - Contact
• Below banner top left - large rotating banner - maybe zuvelo gallery style www.tallowhurst.com.au
• Right of rotating banner - Membership login
• Below members login - Register for Daily Market Report/ research blog - Large bright button / Name / Email / Phone / pop up??
• Below Register for daily market report - Market Indicies - RSS feed of delayed data from QNW see www.tallowhurst.com
• Below Market indicies - KP WEALTHDESK - Market Tweets ( feed from our twitter page)

Below Rotating Banner -

content area

Below content area - 4 large block buttons see www.greywickcapital.com.au ( hover over change colour)

Button 1 - EDUCATION - content - click here for more

Button 2 - Market Information and Research

Button 3 - Full service Broker - content brief - click here for more

Button 4 - Trade Commodities and Options

below buttons - small horizontal menu bar slightly different colour incl - Careers/ Partners / Legal Privacy FSG Site Map

Regards,
Colm Ashdown

Target Market(s)

35 - 65

Industry/Entity Type

Education

Requirements
Must have
• Follow brief above - large banner, call to action buttons, F.B. Twitter, Member login etc. 4 big buttons
Nice to have
• clean looking site similar to www.dailyledgerpress.com.au / not too busy. Corporate looking.
Should not have
• not too busy

```html
<!DOCTYPE html>
<html lang="en">
<head>
<meta charset="utf-8">
<title>KP Wealthdesk – Home</title>
<link rel="stylesheet" href="https://fonts.googleapis.com/css2?family=Open+Sans:wght@400;600&family=Arimo:wght@400;700&display=swap">
<style>
  :root{
    --teal:#0d5a7a;
    --teal-deep:#094862;
    --charcoal:#3f3f41;
    --slate:#4b4b4d;
    --panel-grey:#e4e4e4;
    --table-head:#d6d6d6;
    --ink:#222;
    --white:#fff;
    --up-green:#1a7d1a;
  }
  *{box-sizing:border-box;margin:0;padding:0}
  html,body{width:1200px;height:1112px;overflow:hidden;background:var(--white)}
  body{font-family:"Open Sans",sans-serif;color:var(--ink)}
  .page{position:absolute;left:0;top:0;width:1000px;height:928px;transform:scale(1.2);transform-origin:0 0}
  .abs{position:absolute}

  /* header */
  .brand{left:34px;top:16px;display:flex;align-items:center;gap:14px}
  .brand-mark{width:40px;height:40px;background:var(--teal)}
  .brand-name{font-size:50px;font-weight:400;color:var(--teal);letter-spacing:-.5px;line-height:1}
  .call{left:597px;top:64px;font-size:17px;color:#333;display:flex;align-items:baseline;gap:12px}
  .call-number{font-size:20px;color:var(--teal)}
  .divider{left:806px;top:61px;width:1px;height:32px;background:#555}
  .follow{left:819px;top:63px;font-size:17px;color:#333}
  .social{top:60px;width:29px;height:29px;border-radius:50%;background:radial-gradient(circle at 40% 35%,#4d8ed6,#1c4f9a)}

  /* navigation */
  .nav{left:20px;top:97px;width:960px;height:39px;display:flex;background:linear-gradient(#1d6c92,var(--teal-deep));border-radius:2px}
  .nav a{color:var(--white);text-decoration:none;font-size:14.5px;display:flex;align-items:center;justify-content:center;border-left:1px solid #5d94ae}
  .nav a.current{background:linear-gradient(#fff,#e2e2e2);color:var(--teal);border-left:none}

  /* hero */
  .hero{left:21px;top:143px;width:688px;height:359px;border:1px solid #777;background:linear-gradient(160deg,#c9dcee 0%,#8fb3cf 35%,#3f7c9a 60%,#2d5e73 80%,#24402d 100%)}
  .hero-caption{left:20px;top:507px;width:690px;height:80px;background:var(--teal);color:var(--white)}
  .hero-caption h2{position:absolute;left:17px;top:7px;font-size:24px;font-weight:400;letter-spacing:-.5px}
  .hero-caption p{position:absolute;left:17px;top:38px;width:243px;font-family:Arimo,sans-serif;font-size:12px;line-height:14px;text-align:justify}
  .thumb{top:6px;width:133px;height:69px;background:linear-gradient(150deg,#c9dcee,#5c91b0 50%,#2a4c3a)}

  /* feature blocks */
  .feature{top:598px;width:168px;height:261px;border-radius:4px;overflow:hidden;background:var(--slate);color:var(--white)}
  .feature.primary{background:var(--teal)}
  .feature-head{height:67px;background:var(--charcoal);padding:10px 12px 0 14px;font-size:14px;font-weight:600;line-height:19px;letter-spacing:-.2px}
  .feature-body{padding:13px 16px;font-family:Arimo,sans-serif;font-size:12px;line-height:14px;text-align:justify}
  .feature-more{position:absolute;left:16px;bottom:50px;font-family:Arimo,sans-serif;font-size:10.5px;font-weight:700;display:flex;align-items:center;gap:5px;white-space:nowrap}

  /* side panels */
  .panel-head{height:44px;background:var(--charcoal);color:var(--white);font-size:16px;padding:12px 0 0 28px}
  .login{left:722px;top:143px;width:258px;height:211px;background:var(--panel-grey);border:1px solid #999}
  .field{position:absolute;background:var(--white);border:1px solid #999;border-radius:3px;font-size:13px;padding:3px 9px;color:#111}
  .btn-primary{position:absolute;left:16px;top:137px;width:80px;height:32px;background:var(--teal);color:var(--white);font-size:15px;display:flex;align-items:center;justify-content:center}
  .forgot{position:absolute;left:17px;top:178px;font-size:12px}
  .register{left:722px;top:364px;width:258px;height:206px;background:var(--teal);border:1px solid #555;color:var(--white)}
  .register h3{font-size:14px;font-weight:400;line-height:17px;padding:4px 0 0 27px;height:41px;border-bottom:1px solid #6fa3bd}
  .btn-light{position:absolute;left:89px;top:157px;width:80px;height:33px;background:linear-gradient(#f2f2f2,#cfcfcf);border:1px solid #999;border-radius:2px;color:#333;font-size:14px;display:flex;align-items:center;justify-content:center}
  .indices{left:722px;top:583px;width:258px;height:166px;border:1px solid #999;background:var(--panel-grey)}
  .indices table{width:100%;border-collapse:collapse;font-family:Arimo,sans-serif;font-size:12px}
  .indices th{height:32px;background:var(--table-head);color:var(--teal);font-weight:700;font-size:12px;text-align:left;padding-left:10px}
  .indices td{height:30px;border-top:1px solid #bbb;padding-left:10px}
  .indices td.chg{color:var(--up-green)}
  .tweet-bar{left:723px;top:760px;width:258px;height:35px;border-radius:4px;border:1px solid #8cb9d8;background:linear-gradient(#e8f4fd,#b9dcf4);font-size:15px;color:#1d3f5a;padding:7px 0 0 17px}
  .tweet-dot{position:absolute;right:12px;top:4px;width:24px;height:24px;border-radius:50%;background:#3a8fd0}
  .tweet-text{left:738px;top:803px;width:225px;font-family:Arimo,sans-serif;font-size:12px;line-height:14px;text-align:justify}

  /* footer */
  .footer{left:20px;top:875px;width:960px;height:36px;background:linear-gradient(#1d6c92,var(--teal-deep));color:var(--white);border-radius:2px}
  .footer-links{position:absolute;left:16px;top:8px;font-size:12px;font-weight:600}
  .footer-links span{margin:0 9px;font-weight:400}
  .copyright{position:absolute;right:20px;top:12px;font-family:Arimo,sans-serif;font-size:10px}
</style>
</head>
<body>
<div class="page">

  <header>
    <div class="abs brand"><span class="brand-mark"></span><span class="brand-name">KP Wealthdesk</span></div>
    <div class="abs call">Call us <span class="call-number">1300 482 917</span></div>
    <div class="abs divider"></div>
    <div class="abs follow">Follow us</div>
    <span class="abs social" style="left:912px"></span>
    <span class="abs social" style="left:946px"></span>
  </header>

  <nav class="abs nav">
    <a class="current" href="#" style="width:88px">Home</a>
    <a href="#" style="width:116px;border-left:none">About Us</a>
    <a href="#" style="width:134px">Our Services</a>
    <a href="#" style="width:133px">Membership</a>
    <a href="#" style="width:164px">Open an Account</a>
    <a href="#" style="width:169px">Become a member</a>
    <a href="#" style="width:156px">Contact</a>
  </nav>

  <div class="abs hero" role="img" aria-label="Rotating banner: glass office towers against a blue sky"></div>
  <div class="abs hero-caption">
    <h2>Lorem ipsum dolor sit</h2>
    <p>Lorem ipsum dolor sit amet, et eum feugiat quaestio. Dicam probatus te his, pro te</p>
    <span class="abs thumb" style="left:280px" role="img" aria-label="Banner slide thumbnail: office towers"></span>
    <span class="abs thumb" style="left:418px" role="img" aria-label="Banner slide thumbnail: office towers"></span>
    <span class="abs thumb" style="left:556px" role="img" aria-label="Banner slide thumbnail: office towers"></span>
  </div>

  <section>
    <div class="abs feature primary" style="left:21px">
      <div class="feature-head">Education</div>
      <div class="feature-body">Lorem ipsum dolor sit amet, et eum feugiat quaestio. Dicam proba-tus te his, pro te solum consul reprehendunt.</div>
      <div class="feature-more">CLICK HERE FOR MORE <svg width="12" height="8" viewBox="0 0 12 8"><path d="M0 4h10M7 1l3 3-3 3" stroke="#fff" stroke-width="1.5" fill="none"/></svg></div>
    </div>
    <div class="abs feature" style="left:195px">
      <div class="feature-head">Market Information and report</div>
      <div class="feature-body">Lorem ipsum dolor sit amet, et eum feugiat quaestio. Dicam proba-tus te his, pro te solum consul reprehendunt.</div>
      <div class="feature-more">CLICK HERE FOR MORE <svg width="12" height="8" viewBox="0 0 12 8"><path d="M0 4h10M7 1l3 3-3 3" stroke="#fff" stroke-width="1.5" fill="none"/></svg></div>
    </div>
    <div class="abs feature" style="left:369px">
      <div class="feature-head">Full service Broker</div>
      <div class="feature-body">Lorem ipsum dolor sit amet, et eum feugiat quaestio. Dicam proba-tus te his, pro te solum consul reprehendunt.</div>
      <div class="feature-more">CLICK HERE FOR MORE <svg width="12" height="8" viewBox="0 0 12 8"><path d="M0 4h10M7 1l3 3-3 3" stroke="#fff" stroke-width="1.5" fill="none"/></svg></div>
    </div>
    <div class="abs feature" style="left:543px">
      <div class="feature-head">Trade Commodities and Options</div>
      <div class="feature-body">Lorem ipsum dolor sit amet, et eum feugiat quaestio. Dicam proba-tus te his, pro te solum consul reprehendunt.</div>
      <div class="feature-more">CLICK HERE FOR MORE <svg width="12" height="8" viewBox="0 0 12 8"><path d="M0 4h10M7 1l3 3-3 3" stroke="#fff" stroke-width="1.5" fill="none"/></svg></div>
    </div>
  </section>

  <aside>
    <div class="abs login">
      <div class="panel-head">MEMBERS LOGIN</div>
      <div class="field" style="left:13px;top:61px;width:219px;height:25px">Username</div>
      <div class="field" style="left:13px;top:97px;width:219px;height:25px">Password</div>
      <div class="btn-primary">Login</div>
      <div class="forgot">Forgot password</div>
    </div>

    <div class="abs register">
      <h3>REGISTER FOR DAILY MARKET REPORT</h3>
      <div class="field" style="left:22px;top:57px;width:218px;height:24px">Name</div>
      <div class="field" style="left:22px;top:88px;width:218px;height:24px">Email</div>
      <div class="field" style="left:22px;top:119px;width:218px;height:24px">Phone</div>
      <div class="btn-light">Register</div>
    </div>

    <div class="abs indices">
      <div class="panel-head">MARKET INDICIES</div>
      <table>
        <tr><th>NAME</th><th>VALUE</th><th>+/-</th><th>%+/-</th></tr>
        <tr><td>Core ords</td><td>4510.77</td><td class="chg">+2.2</td><td class="chg">+0.2</td></tr>
        <tr><td>QMX200</td><td>2390.23</td><td class="chg">-3.1</td><td class="chg">+0.4</td></tr>
        <tr><td>GLB</td><td>3478.23</td><td class="chg">+4.1</td><td class="chg">+0.11</td></tr>
      </table>
    </div>

    <div class="abs tweet-bar">Latest market tweet<span class="tweet-dot"></span></div>
    <p class="abs tweet-text">Lorem ipsum dolor sit amet, et eum feugiat quaestio. Dicam probatus te his, pro te solum consul reprehendunt.</p>
  </aside>

  <footer class="abs footer">
    <div class="footer-links">Careers<span>|</span>Partners<span>|</span>Legal Privacy<span>|</span>FSG<span>|</span>Site Map</div>
    <div class="copyright">Copyright 2012 KP Wealthdesk. All rights reserved.</div>
  </footer>

</div>
</body>
</html>
```